Educational Textbook Covern Design for mostly females

Create a textbook cover (will be white spiral) using the Brandguide.pdf attached. This will be a textbook given to mostly age 18-25 year old women so a modern trendy cute type design is wanted.
The book cover is 8.5" x 11" which will be printed in CMYK full bleed.
The name "LoriPQX's Dental Hygiene Academy" must be on the cover somewhere and "LoriPQX" has to be either the same height or larger height than the "Dental Hygiene Academy"

Please no real life photos such as images of dentists, etc. This should be all created art.

The year "2025" should be in the design as well.

IMPORTANT UPDATED 8/4/2024
These designs should not look too childish. This should be a professional textbook for dental professionals. All the current designs have too much cartoon art.

Target Market(s)

18-25 year old females

Industry/Entity Type

Dentistry

Font styles to use
Other font styles liked:
• See brand guide

Colors
A7469A
B969AE
D3A5CF
EDDBEB
F8F0F9
6B429C
8869AF
B7A5CE
E3DAEB
F3F0F8

Requirements
Should not have
• No photos, should be all art

```html
<!DOCTYPE html>
<html lang="en">
<head>
<meta charset="utf-8">
<title>LoriPQX's Dental Hygiene Academy 2025 – Textbook Cover</title>
<link href="https://fonts.googleapis.com/css2?family=Sniglet:wght@800&display=swap" rel="stylesheet">
<style>
  :root {
    --cover-purple: #9d78b3;
    --pattern-purple: #8a64a8;
    --deep-purple: #4a2a7d;
    --paper-white: #f4f4f4;
  }
  * { margin: 0; padding: 0; box-sizing: border-box; }
  html, body {
    width: 927px;
    height: 1200px;
    overflow: hidden;
    background: var(--cover-purple);
  }
  .cover {
    position: relative;
    width: 927px;
    height: 1200px;
    overflow: hidden;
    font-family: "Sniglet", "Arial Rounded MT Bold", sans-serif;
  }
  .cover__pattern {
    position: absolute;
    inset: 0;
    background: radial-gradient(circle at 50% 40%, var(--cover-purple) 0%, var(--pattern-purple) 140%);
  }
  .cover__frames {
    position: absolute;
    inset: 0;
  }
  .brand-seal {
    position: absolute;
    left: 172px;
    top: 131px;
    width: 582px;
    height: 582px;
    border-radius: 50%;
    background: var(--paper-white);
    display: flex;
    align-items: center;
    justify-content: center;
    text-align: center;
  }
  .brand-seal__name {
    font-weight: 800;
    font-size: 46px;
    line-height: 1.15;
    color: var(--deep-purple);
    letter-spacing: 1px;
    text-transform: uppercase;
  }
  .cover-title {
    position: absolute;
    left: 0;
    right: 0;
    top: 752px;
    text-align: center;
    color: var(--paper-white);
    font-weight: 800;
    line-height: 1;
  }
  .cover-title__line--main {
    display: block;
    font-size: 72px;
    letter-spacing: 0.5px;
  }
  .cover-title__line--sub {
    display: block;
    font-size: 50px;
    margin-top: 20px;
  }
  .cover-title__year {
    display: block;
    font-size: 70px;
    margin-top: 24px;
  }
</style>
</head>
<body>
  <main class="cover">
    <div class="cover__pattern" role="img" aria-label="Repeating pattern of cartoon tooth characters with glasses, graduation caps, microphones and party hats in soft purple and gold tones"></div>

    <svg class="cover__frames" width="927" height="1200" viewBox="0 0 927 1200" aria-hidden="true">
      <g fill="none" stroke="var(--paper-white)" stroke-width="5">
        <polyline points="155,541 70,541 70,1098 854,1098 854,541 772,541"/>
        <polyline points="155,565 100,565 100,1069 824,1069 824,565 772,565"/>
      </g>
    </svg>

    <div class="brand-seal">
      <p class="brand-seal__name">LoriPQX's<br>Dental Hygiene<br>Academy</p>
    </div>

    <h1 class="cover-title">
      <span class="cover-title__line--main">LoriPQX's Dental</span>
      <span class="cover-title__line--sub">Hygiene Academy</span>
      <span class="cover-title__year">2025</span>
    </h1>
  </main>
</body>
</html>
```